Awesome Professional Template for a collaborative report

File format: A4 PDF ideally

Design Requirements:

3 or 4 variants of a template some with graphics and pull quotes and a bio page for the essayists with a profile pic and a short descriptor

Layout Format: PPT would be perfect ideally portrait format

Style/Reference Guide: Varnholt or QM styles thought leadership reports as a guide

We need to input 10 essays around a specific subject with a nice layout with place holders for high impact pull quotes from the copy, stunning colourway and typrography probably A4 format but emailed as a PDF ideally not a huge file size. Striking front cover with title and list of contributors plus layout variations for the essays which will include a head shot short profile and contacts for the authors. Ideally a portrait format PPT that is easy to work with.

Target Market(s)

business professionals in brands

Industry/Entity Type

brand marketing

Font styles to use
Sans Serif

Colors
0054AA
0677BA
7BADD7
CADEEF
E8F1F8
00AB8E
00BBA5
67D7C9
C6EFE9
E9F9F6
F0912C
F2A743
F7CA91
FBE8D2
FDF5EE
6B429C
8869AF
B7A5CE
E3DAEB
F3F0F8

Requirements
Must have
• awesome visual impact

```html
<!DOCTYPE html>
<html lang="en">
<head>
<meta charset="utf-8">
<title>Collaborative Report – Essay Spread</title>
<link rel="stylesheet" href="https://fonts.googleapis.com/css2?family=Poppins:ital,wght@0,300;0,400;0,500;0,600;1,400;1,500;1,600&display=swap">
<style>
  :root {
    --bg: #e2e3e4;
    --paper: #ffffff;
    --ink: #1f2226;
    --ink-soft: #3a3e44;
    --orange: #f2a743;
    --orange-light: #f7ca91;
    --teal: #00ab8e;
    --teal-bright: #00bba5;
    --teal-pale: #e9f9f6;
    --teal-mist: #c6efe9;
    --purple: #6b429c;
    --blue-deep: #0054aa;
    --blue: #0677ba;
    --blue-light: #7badd7;
    --wave-end: #c9d6dc;
  }
  * { box-sizing: border-box; margin: 0; padding: 0; }
  html, body {
    width: 1200px; height: 800px; overflow: hidden;
    background: var(--bg);
    font-family: "Poppins", sans-serif;
    color: var(--ink);
  }
  .spread {
    position: absolute; left: 77px; top: 30px;
    width: 1046px; height: 740px;
    display: flex;
    box-shadow: 0 10px 30px rgba(0,0,0,.12);
  }
  .page {
    position: relative; width: 523px; height: 740px;
    background: var(--paper); overflow: hidden;
  }
  .page--left { box-shadow: inset -14px 0 18px -14px rgba(0,0,0,.14); }
  .page--right { box-shadow: inset 14px 0 18px -14px rgba(0,0,0,.14); }

  .section-mark {
    position: absolute; top: 28px; width: 18px; height: 18px;
    border-radius: 50%; background: var(--teal-bright);
  }
  .page--left .section-mark { right: 28px; }
  .page--right .section-mark { right: 40px; }

  /* Left page */
  .essay-title {
    position: absolute; left: 46px; top: 56px;
    font-size: 22px; font-weight: 600; color: var(--orange-light);
    letter-spacing: .2px;
  }
  .subhead {
    font-size: 9.5px; font-weight: 600; color: var(--orange-light);
    margin-bottom: 2px;
  }
  .body-lg { font-size: 9.6px; line-height: 1.38; color: var(--ink); }
  .body-sm { font-size: 8.1px; line-height: 1.5; color: var(--ink-soft); }
  .intro { position: absolute; left: 72px; top: 96px; width: 395px; }

  .feature-image {
    position: absolute; left: 0; top: 204px; width: 268px; height: 270px;
    background: linear-gradient(140deg, #3f6b93 0%, #7ea2b3 30%, #c6c99a 52%, #c9a74a 70%, #223f74 100%);
  }
  .side-column { position: absolute; left: 284px; top: 204px; width: 210px; }
  .side-column p { margin-bottom: 10px; }
  .side-column .subhead { margin-top: 4px; }

  .lower-text { position: absolute; left: 72px; top: 490px; width: 410px; }
  .lower-text p { margin-bottom: 11px; }

  .byline { font-size: 9.6px; margin-top: 14px; }
  .stats { font-size: 9.6px; margin-top: 10px; }

  /* Right page */
  .essay-title--teal {
    position: absolute; left: 40px; top: 50px; width: 260px;
    font-size: 17px; line-height: 1.15; font-weight: 600; font-style: italic;
    color: var(--teal);
  }
  .right-text { position: absolute; left: 40px; top: 104px; width: 440px; }
  .right-text .subhead { color: var(--teal); font-style: italic; font-size: 8.6px; margin-top: 10px; }
  .right-text .subhead:first-child { margin-top: 0; }
  .right-text p { margin-bottom: 8px; }
  .right-text .lead { font-style: italic; }
  .right-text .byline { font-size: 8.4px; font-style: italic; margin-top: 12px; }
  .right-text .stats { font-size: 8.4px; margin-top: 6px; font-style: italic; }

  .quote-panel { position: absolute; left: 0; bottom: 0; width: 523px; height: 330px; }
  .quote-panel svg { position: absolute; inset: 0; }
  .pull-quote {
    position: absolute; left: 56px; top: 110px; width: 410px;
    font-size: 17.5px; line-height: 1.4; font-weight: 300; color: var(--teal);
  }
  .quote-mark {
    font-weight: 700; font-size: 34px; line-height: 0; color: var(--teal);
    vertical-align: -12px;
  }
  .quote-mark--open { margin-right: 6px; }
  .quote-mark--close { margin-left: 6px; }
  .quote-credit { margin-top: 14px; font-size: 9px; font-weight: 400; color: var(--ink-soft); }
</style>
</head>
<body>
  <main class="spread">
    <section class="page page--left">
      <span class="section-mark"></span>
      <h1 class="essay-title">More value in data</h1>

      <div class="intro">
        <h2 class="subhead">What is Deep Learning?</h2>
        <p class="body-lg">In the last decade, we started to hear an interesting and intriguing term – artificial intelligence very often. This term is everywhere, we hear it all the time in our surroundings and it’s not surprising to us anymore. Artificial intelligence became a natural part of life. A lot of tools, technologies, and software that we are using every day are based on AI.</p>
      </div>

      <div class="feature-image" role="img" aria-label="Essay photograph: close-up of a blue, cream and gold mosaic wall"></div>

      <div class="side-column body-sm">
        <p>The progress wasn’t felt so strongly like the last couple of decades. While we tried to understand artificial intelligence’s pros and cons and discuss ethical aspects the science jumped to a new stage – machine learning and even furthermore – deep learning. In simple words, deep learning is a subset of machine learning, and machine learning is a subset of Artificial Intelligence.</p>
        <h2 class="subhead">AI and Neuroscience</h2>
        <p>The same situation happened with marketing. All of us know something about marketing in general, later we became familiar with digital marketing, today we are further talking about Consumer Neuroscience and Neuromarketing. Over the last 5 decades, predictive analytics have become pivotal as a decision-making tool, but its initial conception reaches back much further. It all began back in 1689 with Harrow’s of London insurance market. Whilst the processes were not as sophisticated and couldn’t quite predict as much as they can</p>
      </div>

      <div class="lower-text body-lg">
        <p>now, the original premise remains the same; Predictive analytics is a mathematical modelling tool that relies on historical data, data mining and machine learning to forecast outcomes.</p>
        <p>Here we explore 5 Predictive Analytics Techniques and Predictive Analytics Modelling and how these tools can be a highly effective way of compiling data into projected insights that can be implemented across your brand.</p>
        <p>Why here are we talking about AI and neuroscience? The reason is simple – predicted eye-tracking tools which are based on AI and close related to neurosciences. More insights about neuroscience are in the article “What are the possibilities of neuromarketing now and in the future?”</p>
        <p class="byline">Daniel Whitcombe</p>
        <p class="stats">Characters: 2017 Words: 319 Lines: 44 Paragraphs: 9</p>
      </div>
    </section>

    <section class="page page--right">
      <span class="section-mark"></span>
      <h1 class="essay-title--teal">Why Predictive Analytics is Important</h1>

      <div class="right-text body-sm">
        <h2 class="subhead">What is Predictive Analytics?</h2>
        <p class="lead">Over the last 5 decades, predictive analytics have become pivotal as a decision-making tool, but its initial conception reaches back much further. It all began back in 1689 with Harrow’s of London insurance market. Whilst the processes were not as sophisticated and couldn’t quite predict as much as they can now, the original premise remains the same; Predictive analytics is a mathematical modelling tool that relies on historical data, data mining and machine learning to forecast outcomes.</p>
        <p class="lead">Here we explore 5 Predictive Analytics Techniques and Predictive Analytics Modelling and how these tools can be a highly effective way of compiling data into projected insights that can be implemented across your brand.</p>
        <h2 class="subhead">Predictive Analytics Techniques</h2>
        <p class="lead">There are hundreds of predictive analytics techniques that you can integrate with data for forecasting results. We’re going to focus on just five to explore just how different the techniques are:</p>
        <h2 class="subhead">Neural Networks</h2>
        <p class="lead">This technique is highly sophisticated and can handle relationships in data that are sourced from multiple origins. Neural networks are mighty because they are based on AI processes and the recognition of patterns that outline parameters. They were initially developed as a way to copy the human brain’s neural functions.</p>
        <p class="byline">Daniel Whitcombe</p>
        <p class="stats">Characters: 1304 Words: 201 Lines: 22 Paragraphs: 7</p>
      </div>

      <div class="quote-panel">
        <svg viewBox="0 0 523 330" width="523" height="330" aria-hidden="true">
          <defs>
            <linearGradient id="waveFill" x1="0" y1="0" x2="1" y2="1">
              <stop offset="0" stop-color="#e9f9f6"/>
              <stop offset="1" stop-color="#c9d6dc"/>
            </linearGradient>
          </defs>
          <path d="M0 70 C 120 10, 260 20, 360 40 S 480 60, 523 30 L 523 330 L 0 330 Z" fill="url(#waveFill)"/>
        </svg>
        <blockquote class="pull-quote">
          <span class="quote-mark quote-mark--open">“</span>We need to input 10 for high impact pull quotes from the copy, stunning colourway and typography probably A4 format but emailed cover with title and list of contributors plus layout easy to work with.<span class="quote-mark quote-mark--close">”</span>
          <p class="quote-credit">Daniel Whitcombe</p>
        </blockquote>
      </div>
    </section>
  </main>
</body>
</html>
```